Lotus Reed Kitchen Road Billboard

Road Billboard I need all of this information on it
Authentic Thai Food Bangkok Style
6.5 Miles on the right
4172 Marlow Rd Pelham NC
828-555-0147

```html
<!DOCTYPE html>
<html lang="en">
<head>
<meta charset="utf-8">
<title>Lotus Reed Kitchen Road Billboard</title>
<link rel="stylesheet" href="https://fonts.googleapis.com/css2?family=Saira+Condensed:wght@500;600;700&display=swap">
<style>
  :root {
    --canvas-bg: #d4d4d6;
    --board-black: #000000;
    --brand-gold: #d9ab14;
    --text-white: #ffffff;
    --fire-deep: #1a120c;
    --fire-mid: #7a3410;
    --fire-hot: #f08a1c;
    --wok-grey: #4a4540;
  }
  html, body {
    margin: 0;
    padding: 0;
    width: 1137px;
    height: 1200px;
    overflow: hidden;
    background: var(--canvas-bg);
  }
  .billboard {
    position: absolute;
    left: 40px;
    top: 389px;
    width: 1057px;
    height: 422px;
    display: block;
  }
  .board-text {
    font-family: "Saira Condensed", "Arial Narrow", sans-serif;
  }
  .brand-name { fill: var(--brand-gold); font-weight: 600; font-size: 28px; }
  .brand-dot { fill: var(--brand-gold); }
  .headline-top { fill: var(--brand-gold); font-weight: 600; font-size: 56px; }
  .headline-main { fill: var(--brand-gold); font-weight: 700; font-size: 76px; }
  .address-line { fill: var(--text-white); font-weight: 600; font-size: 46px; }
  .phone-pill { fill: var(--board-black); }
  .phone-number { fill: var(--text-white); font-weight: 700; font-size: 72px; }
  .icon-white { fill: var(--text-white); }
  .icon-stroke { fill: none; stroke: var(--text-white); stroke-width: 4; stroke-linecap: round; }
  .panel-black { fill: var(--board-black); }
  .panel-gold { fill: var(--brand-gold); }
</style>
</head>
<body>
<svg class="billboard" viewBox="0 0 1546 617" xmlns="http://www.w3.org/2000/svg">
  <defs>
    <radialGradient id="fireGlow" cx="0.45" cy="0.6" r="0.7">
      <stop offset="0" stop-color="var(--wok-grey)"/>
      <stop offset="0.35" stop-color="var(--fire-mid)"/>
      <stop offset="0.7" stop-color="var(--fire-deep)"/>
      <stop offset="1" stop-color="var(--board-black)"/>
    </radialGradient>
    <linearGradient id="flameBand" x1="0" y1="1" x2="0" y2="0">
      <stop offset="0" stop-color="var(--fire-hot)" stop-opacity="0.75"/>
      <stop offset="0.45" stop-color="var(--fire-hot)" stop-opacity="0"/>
    </linearGradient>
  </defs>

  <rect class="panel-black" x="0" y="0" width="1546" height="617"/>

  <g class="hero-photo" role="img" aria-label="Photo of shrimp, broccoli and vegetables tossed above a flaming wok">
    <path d="M250,0 C330,0 420,60 410,140 C400,210 360,260 410,320 C450,370 500,400 500,460 C500,540 470,600 420,617 H1546 V0 Z" fill="url(#fireGlow)"/>
    <path d="M250,0 C330,0 420,60 410,140 C400,210 360,260 410,320 C450,370 500,400 500,460 C500,540 470,600 420,617 H1546 V0 Z" fill="url(#flameBand)"/>
  </g>

  <path class="panel-gold" d="M965,0 C930,20 905,60 915,110 C925,170 1000,200 1040,250 C1070,300 1050,360 1040,420 C1030,480 1060,570 1100,617 H1546 V0 Z"/>

  <g class="brand">
    <circle class="brand-dot" cx="141" cy="112" r="26"/>
    <text class="board-text brand-name" x="141" y="187" text-anchor="middle" textLength="178" lengthAdjust="spacingAndGlyphs">Lotus Reed Kitchen</text>
  </g>

  <g class="headline">
    <text class="board-text headline-top" x="42" y="437" textLength="415" lengthAdjust="spacingAndGlyphs">AUTHENTIC THAI FOOD</text>
    <text class="board-text headline-main" x="42" y="510" textLength="416" lengthAdjust="spacingAndGlyphs">BANGKOK STYLE</text>
  </g>

  <g class="directions">
    <path class="icon-white" d="M1024,120 a19,19 0 0 1 19,19 c0,15 -19,38 -19,38 c0,0 -19,-23 -19,-38 a19,19 0 0 1 19,-19 z M1024,131 a8,8 0 1 0 0.01,0 z" fill-rule="evenodd"/>
    <text class="board-text address-line" x="1063" y="144" textLength="362" lengthAdjust="spacingAndGlyphs">6.5 Miles on the right</text>
    <text class="board-text address-line" x="1063" y="203" textLength="432" lengthAdjust="spacingAndGlyphs">4172 Marlow Rd Pelham NC</text>
  </g>

  <g class="phone">
    <rect class="phone-pill" x="1035" y="347" width="465" height="138" rx="69"/>
    <g transform="translate(1070,396) scale(0.8)">
      <path class="icon-white" d="M2,4 c4,-4 9,-4 12,0 l7,9 c2,3 1,7 -2,9 l-4,3 c3,8 9,14 17,17 l3,-4 c2,-3 6,-4 9,-2 l9,7 c4,3 4,8 0,12 l-5,4 c-6,5 -20,2 -33,-11 c-13,-13 -16,-27 -11,-33 z"/>
      <path class="icon-stroke" d="M32,8 a14,14 0 0 1 12,12 M34,-4 a26,26 0 0 1 22,22"/>
    </g>
    <text class="board-text phone-number" x="1124" y="441" textLength="348" lengthAdjust="spacingAndGlyphs">828-555-0147</text>
  </g>
</svg>
</body>
</html>
```